clean web design for a recruitment company

We need a web design for a company called 'TORAVI' recruitment. We are a new age recruitment companies that selects people by their true nature, values and what they can bring to the table as a tangible talent. We are all here possessing a certain talent, whatever that could be that the world needs. The final design should communicate professionalism and strongly embedded etiquette we believe in and a branding promise 'Seeing ones true nature'. Our companies values are integrity, giving away to the community, cherishing the sharing of our talent, time and helping one another.

Target Market(s)

Gulf Countries

Industry/Entity Type

It Company

Number of Pages Required

1 page

Font styles to use
Serif

Requirements
Must have
• Clear and readable font, user friendly structure and easy navigation menus.
Nice to have
• Extra sort of ideas on images we may use, tag lines etc. sample sites we love site:https://www.velmorandi.example/
• http://www.tessabrankow.example/
• http://www.pebbleloomcraft.example/idea-gallery/
Should not have
• all sort of colors, big combination of fonts, images with people in the office or people in suits likewise all the typical industry web sites

```html
<!DOCTYPE html>
<html lang="en">
<head>
<meta charset="utf-8">
<title>Toravi Recruitment</title>
<link href="https://fonts.googleapis.com/css2?family=PT+Serif:wght@400;700&display=swap" rel="stylesheet">
<style>
  :root{
    --page:#f1f2f1;
    --panel:#ffffff;
    --ink:#2c2c2c;
    --body:#5a5a5a;
    --nav-bg:#d6d6d6;
    --nav-line:#9a9a9a;
    --header-bg:#cfcfcf;
    --footer:#7f7f7f;
    --footer-ink:#ffffff;
    --tile:#ededed;
    --tile-frame:#c9c9c9;
  }
  *{box-sizing:border-box;margin:0;padding:0}
  html,body{width:768px;height:1200px;overflow:hidden}
  body{position:relative;background:var(--page);font-family:"PT Serif",Georgia,serif;color:var(--ink)}
  .abs{position:absolute}

  .hero-backdrop{left:0;top:0;width:768px;height:377px;
    background:
      linear-gradient(90deg,rgba(40,38,35,.85) 0%,rgba(40,38,35,0) 9%,rgba(40,38,35,0) 91%,rgba(40,38,35,.85) 100%),
      linear-gradient(180deg,#a8a6a1 0%,#c4c2bd 25%,#9d9a94 60%,#5a544c 85%,#3c3833 100%)}
  .header{left:84px;top:0;width:598px;height:116px;background:var(--header-bg)}
  .brand{left:84px;top:0;width:104px;height:116px;background:#d9d9d9;border-right:1px solid var(--nav-line);
    display:flex;flex-direction:column;align-items:center;justify-content:flex-end;padding-bottom:8px;gap:8px}
  .brand-mark{width:34px;height:34px;background:#2b2b2b;position:absolute;top:12px;left:35px}
  .brand-name{font-size:23px;font-weight:700;color:#2b2b2b;letter-spacing:1px;line-height:1}
  .brand-tag{font-size:8px;letter-spacing:2.6px;color:#2b2b2b;line-height:1}
  .header-rule{left:188px;top:24px;width:494px;height:1px;background:#7a7a7a}
  .social{top:0;height:24px;display:flex}
  .social span{width:27px;height:24px;border-left:1px solid #9a9a9a;display:flex;align-items:center;justify-content:center}
  .social span i{width:12px;height:12px;border-radius:50%;background:#8a8a8a;display:block}
  .nav{left:188px;top:91px;width:494px;height:25px;display:flex;list-style:none;background:var(--nav-bg);border-top:1px solid var(--nav-line)}
  .nav li{font-size:11px;line-height:24px;border-right:1px solid var(--nav-line);text-align:center}
  .nav li.active{background:#f4f4f4}

  .hero-photo{left:85px;top:128px;width:597px;height:208px;
    background:
      radial-gradient(ellipse 22% 60% at 55% 62%,rgba(40,36,32,.55) 0%,rgba(40,36,32,0) 100%),
      linear-gradient(180deg,
        #e6e4df 0%,#e6e4df 6%,
        #8e8b86 8%,#5d5a56 22%,#6e6b66 35%,#8f8c87 38%,
        #d9d6d0 40%,#c9c6c0 62%,
        #3a3632 64%,#4a4038 70%,#6a5644 82%,#4c3d2f 100%)}
  .credit{left:526px;top:214px;width:138px;height:105px;background:rgba(220,220,220,.45);color:#fff;padding:10px}
  .credit .service{font-size:15px;font-weight:700}
  .credit .by{position:absolute;left:10px;top:70px;font-size:8px}
  .credit .who{position:absolute;left:10px;top:84px;font-size:7px;font-weight:700}
  .dots{left:655px;top:327px;display:flex;gap:4px}
  .dots i{width:4px;height:4px;border-radius:50%;background:#fff;display:block}
  .scroll-cue{left:360px;top:350px}

  .intro{left:84px;top:377px;width:402px;height:119px;background:var(--panel);padding:12px 11px;font-size:10.3px;line-height:12.2px;color:var(--body)}
  .intro p+p{margin-top:12px}
  .mood-photo{left:84px;top:496px;width:402px;height:141px;
    background:
      radial-gradient(ellipse 20% 70% at 50% 45%,#a9a9a9 0%,#7a7a7a 40%,rgba(70,70,70,0) 100%),
      linear-gradient(90deg,#454545 0%,#4d4d4d 35%,#2e2e2e 70%,#484848 100%)}
  .venue-photo{left:486px;top:377px;width:196px;height:260px;
    background:
      radial-gradient(ellipse 38% 22% at 52% 16%,#e8e8e8 0%,#9a9a9a 55%,rgba(60,60,60,0) 100%),
      linear-gradient(180deg,#1e1e1e 0%,#5a5a5a 20%,#b8b8b8 32%,#7d7d7d 40%,#d4d4d4 52%,#6e6e6e 70%,#2c2c2c 100%)}
  .credit.small{left:569px;top:490px;width:100px;height:133px;padding:8px}
  .credit.small .service{font-size:12px;margin-top:40px}
  .credit.small .by{top:106px;left:8px}
  .credit.small .who{top:118px;left:8px}

  .tiles-backdrop{left:0;top:637px;width:768px;height:113px;background:linear-gradient(90deg,#4a3f3a 0%,#8c8580 10%,#c8c6c4 13%,#c8c6c4 87%,#8c8580 90%,#4a3f3a 100%)}
  .tiles{left:84px;top:637px;width:598px;height:113px;display:flex;background:#cbcbcb}
  .tile{flex:1;border-right:1px solid #a9a9a9;display:flex;align-items:center;justify-content:center}
  .tile:last-child{border-right:0}
  .tile-face{width:118px;height:93px;background:var(--tile);border:2px solid var(--tile-frame);display:flex;align-items:center;justify-content:center;font-size:13px;color:var(--ink);position:relative}
  .tile-face.active{background:#fff}
  .tile-face.active span{border-bottom:1px solid #999;padding-bottom:1px}
  .tile-face svg{position:absolute;bottom:8px;left:50%;margin-left:-9px}

  .concept{left:84px;top:760px;width:598px;height:222px;background:var(--panel)}
  .concept h2{position:absolute;left:0;width:598px;top:7px;text-align:center;font-weight:400;font-size:17px}
  .concept .sub{position:absolute;left:0;width:598px;top:29px;text-align:center;font-size:9.5px}
  .concept .col{position:absolute;top:56px;width:272px;font-size:10px;line-height:12.2px;color:var(--body)}
  .concept .col p+p{margin-top:12px}

  .footer{left:0;top:990px;width:768px;height:210px;background:var(--footer);color:var(--footer-ink)}
  .footer h3{position:absolute;top:16px;font-weight:400;font-size:13px}
  .footer address{position:absolute;top:47px;font-style:normal;font-size:13px;line-height:15.5px}
  .field{position:absolute;left:496px;width:183px;height:23px;background:#fff}
  .submit{position:absolute;left:618px;top:150px;width:61px;height:23px;background:linear-gradient(#f3f3f3,#bdbdbd);color:#333;font-size:9px;text-align:center;line-height:23px}
  .footer-rule{position:absolute;left:84px;top:181px;width:598px;height:1px;background:#a5a5a5}
  .copyright{position:absolute;left:84px;top:185px;font-size:9px;color:#444}
</style>
</head>
<body>
  <div class="abs hero-backdrop" role="img" aria-label="Blurred gallery hall backdrop"></div>
  <header>
    <div class="abs header"></div>
    <div class="abs brand">
      <i class="brand-mark"></i>
      <span class="brand-name">toravi</span>
      <span class="brand-tag">RECRUITMENT</span>
    </div>
    <div class="abs header-rule"></div>
    <div class="abs social" style="left:600px"><span><i></i></span><span><i></i></span><span><i></i></span></div>
    <ul class="abs nav">
      <li class="active" style="width:47px">Home</li>
      <li style="width:46px">Team</li>
      <li style="width:83px">Methodology</li>
      <li style="width:93px">Specialist Areas</li>
      <li style="width:53px">Clients</li>
      <li style="width:70px">Candidates</li>
      <li style="width:102px;border-right:0">Toravi Group</li>
    </ul>
  </header>

  <div class="abs hero-photo" role="img" aria-label="Gallery wall of framed black and white fashion portraits with a visitor walking past"></div>
  <div class="abs credit"><div class="service">Pixloom</div><div class="by">Published by</div><div class="who">lenavoss</div></div>
  <div class="abs dots"><i></i><i></i><i></i></div>
  <svg class="abs scroll-cue" width="24" height="12" viewBox="0 0 24 12"><path d="M1 1 L12 10 L23 1" fill="none" stroke="#fff" stroke-width="1.6"/></svg>

  <section>
    <div class="abs intro">
      <p>Praesent rhoncus massa ut diam rutrum, sed cursus tortor cursus. Sed eu enim eu nunc aliquet posuere sed ac ipsum. Donec tincidunt enim in elit aliquam euismod. Phasellus consequat erat dui, ut lacinia lacus dapibus quis.</p>
      <p>Praesent rhoncus massa ut diam rutrum, sed cursus tortor cursus. Sed eu enim eu nunc aliquet posuere sed ac ipsum. Donec tincidunt enim in elit aliquam euismod. Phasellus consequat erat dui, ut lacinia lacus dapibus quis.</p>
    </div>
    <div class="abs mood-photo" role="img" aria-label="Dark monochrome portrait photograph"></div>
    <div class="abs venue-photo" role="img" aria-label="Black and white view of an arched gallery interior"></div>
    <div class="abs credit small"><div class="service">Pixloom</div><div class="by">Published by</div><div class="who">marlowe116</div></div>
  </section>

  <div class="abs tiles-backdrop" role="img" aria-label="Blurred interior backdrop"></div>
  <nav class="abs tiles">
    <div class="tile"><div class="tile-face active"><span>Concept</span><svg width="18" height="9" viewBox="0 0 18 9"><path d="M1 1 L9 8 L17 1" fill="none" stroke="#aaa" stroke-width="1.6"/></svg></div></div>
    <div class="tile"><div class="tile-face">Values</div></div>
    <div class="tile"><div class="tile-face">Social</div></div>
    <div class="tile"><div class="tile-face">Dubai 2020</div></div>
  </nav>

  <section class="abs concept">
    <h2>Placement Concept Text</h2>
    <div class="sub">More Placement Text</div>
    <div class="col" style="left:10px">
      <p>Praesent rhoncus massa ut diam rutrum, sed cursus tortor cursus. Sed eu enim eu nunc aliquet posuere sed ac ipsum. Donec tincidunt enim in elit aliquam euismod. Phasellus consequat erat dui, ut lacinia lacus dapibus quis.</p>
      <p>Nunc varius facilisis mauris id maximus. Integer ac accumsan sapien, ut aliquam orci. Etiam sit amet elementum nibh, at dapibus purus. Vivamus scelerisque venenatis orci, eget luctus tellus iaculis sit amet. Curabitur congue justo ante, a condimentum ex posuere eu. Etiam finibus id sapien vel sodales.</p>
    </div>
    <div class="col" style="left:316px">
      <p>Praesent rhoncus massa ut diam rutrum, sed cursus tortor cursus. Sed eu enim eu nunc aliquet posuere sed ac ipsum. Donec tincidunt enim in elit aliquam euismod. Phasellus consequat erat dui, ut lacinia lacus dapibus quis.</p>
    </div>
  </section>

  <footer class="abs footer">
    <h3 style="left:85px">OFFICE LOCATION</h3>
    <address style="left:85px">Toravi Group<br>14 Linden Walk<br>Paris<br>75011<br>France<br><br>+44 20 7946 0518</address>
    <h3 style="left:293px">CONTACT DETAILS</h3>
    <address style="left:293px">+44 20 7946 0518<br>hello@toravigroup.example</address>
    <h3 style="left:496px">NEWSLETTER SIGN UP</h3>
    <div class="field" style="top:38px"></div>
    <div class="field" style="top:66px"></div>
    <div class="field" style="top:92px"></div>
    <div class="field" style="top:119px"></div>
    <div class="submit">SUBMIT</div>
    <div class="footer-rule"></div>
    <div class="copyright">Copyright 2015 Toravi Group</div>
  </footer>
</body>
</html>
```